Vaultrix Web Site

Hi Designers. Our web site at www.vaultrix.net.au needs a new look.

We do:

- off-site backup, every day, for vital data
- data recovery from crashed disks

We have an existing logo

Our colour is blue. Our image is about Trust and Competence

We are in Perth, Western Australia. Our photographs are local images.

We've been in business for fifteen years.

We have a second URL too: www.keep-our-records.com.au

Both URLs go to the same web site.

Would you like to take on this project?

Target Market(s)

Target market is small to medium business, with between 5 and 100 staff. Customers are mainly in Australia but can be anywhere. There are other providers who are cheaper- our point of difference is that we are highly professional and have been in the business for 15 years. personal attention is important to us- we promise Extreme Service.

Industry/Entity Type

Data Recovery

Requirements
Must have
• Our image is about Trust and Competence. Existing text from our web site can be used.
Should not have
• No moving Flash, no Flash intro

```html
<!DOCTYPE html>
<html lang="en">
<head>
<meta charset="utf-8">
<title>Vaultrix Computer Services</title>
<link rel="stylesheet" href="https://fonts.googleapis.com/css2?family=Open+Sans:ital,wght@0,400;0,600;0,700;1,400;1,700&family=Arimo:ital,wght@0,400;0,700;1,400&display=swap">
<style>
:root{
  --navy:#0d3b66;
  --ink:#12385e;
  --hero-dark:#0c4a82;
  --hero-mid:#1a64a3;
  --tab-top:#5f9ad0;
  --tab-bottom:#1a5a97;
  --panel-bg:#a9cdef;
  --card-top:#e6f0fa;
  --card-bottom:#ffffff;
  --card-border:#c9dcef;
  --footer-bg:#e2edf8;
  --footer-line:#bcd1e6;
  --base-bg:#e8f1fa;
  --muted:#555e66;
}
*{margin:0;padding:0;box-sizing:border-box}
html,body{width:1200px;height:896px;overflow:hidden;background:#fff}
body{position:relative;font-family:"Arimo",Arial,sans-serif;color:var(--ink)}
.abs{position:absolute}

/* header */
.brand{left:123px;top:20px;height:84px;display:flex;align-items:center;gap:18px}
.brand-mark{width:70px;height:70px;border-radius:50%;background:var(--navy)}
.brand-name{font-family:"Open Sans",sans-serif;font-weight:400;font-size:30px;letter-spacing:3px;color:var(--navy);padding-left:16px;border-left:1px solid #c8cdd3;line-height:70px}
.utility{top:5px;right:128px;display:flex;gap:20px;font-size:12px}
.utility a{color:var(--ink);text-decoration:underline;display:flex;align-items:center;gap:7px}
.utility i{display:inline-block;width:14px;height:14px;border-radius:50%;background:#5aa6d8}
.utility a:nth-child(2) i{background:#7f8fa8}
.utility a:nth-child(3) i{background:#4e9a3a}

.nav{left:216px;top:107px;display:flex;gap:1px}
.nav a{width:142px;height:35px;border:1px solid #0f4478;border-bottom:none;border-radius:7px 7px 0 0;background:linear-gradient(var(--tab-top),var(--tab-bottom) 55%,#0f4a86);color:#fff;text-decoration:none;font-family:"Open Sans",sans-serif;font-size:15px;letter-spacing:1.3px;text-align:center;line-height:35px}

/* hero */
.hero{left:0;top:142px;width:1200px;height:225px;background:radial-gradient(ellipse at 30% 40%,var(--hero-mid),var(--hero-dark) 60%,#0b3f70)}
.hero-base{left:0;top:367px;width:1200px;height:81px;background:linear-gradient(#c7d8ea,#f4f8fc);border-top:1px solid #e6eef7;border-bottom:1px solid #b6c8da}
.hero-title{left:148px;top:175px;font-family:"Open Sans",sans-serif;font-weight:700;font-style:italic;font-size:32px;line-height:42px;color:#fff;letter-spacing:-.3px;text-shadow:0 2px 3px rgba(0,0,0,.4)}
.hero-text{left:148px;top:272px;width:490px;font-style:italic;font-size:17px;line-height:21.5px;color:#fff}
.cta{left:146px;top:388px;width:276px;height:50px}
.cta-label{left:175px;top:389px;width:245px;height:36px;border-radius:4px;background:linear-gradient(#d8c2ae,#a98a72);color:#fff;font-weight:700;font-size:19px;line-height:36px;padding-left:48px;text-decoration:none;text-shadow:0 1px 2px rgba(0,0,0,.4)}
.product{left:756px;top:156px;width:288px;height:288px;background:linear-gradient(160deg,#e9eef4,#b8c7d8 60%,#7d95b0);border-radius:4px;opacity:.95}

/* content */
.content{left:0;top:449px;width:1200px;height:356px;background:linear-gradient(var(--panel-bg),#c5def4)}
.card{top:478px;width:303px;height:308px;border:1px solid var(--card-border);border-radius:5px;background:linear-gradient(var(--card-top),var(--card-bottom) 80%)}
.card h2{font-family:"Open Sans",sans-serif;font-style:italic;font-weight:400;font-size:24px;color:var(--ink);position:absolute;left:8px;top:7px;letter-spacing:-.3px}
.card p,.card li{font-size:12px;color:var(--ink)}
.services ul{list-style:none;position:absolute;left:10px;top:49px}
.services li{font-size:11.6px;line-height:29.3px;padding-left:22px;position:relative;white-space:nowrap}
.services li::before{content:"";position:absolute;left:3px;top:12px;width:5px;height:5px;border-top:1.5px solid var(--ink);border-right:1.5px solid var(--ink);transform:rotate(45deg)}
.services{left:123px}
.about{left:446px}
.about p{position:absolute;left:11px;top:51px;width:282px;line-height:17.6px;font-size:11.6px}
.testimonial{left:769px}
.testimonial p{position:absolute;left:18px;top:58px;width:272px;line-height:17.6px;text-indent:38px;font-size:11.6px}
.quote{font-family:Georgia,serif;font-size:50px;color:#9aa3ab;position:absolute;line-height:1}
.quote.open{left:16px;top:40px}
.quote.close{right:16px;top:228px}
.client{position:absolute;left:18px;top:243px;font-weight:700;font-size:12px;color:var(--ink)}
.more{position:absolute;right:14px;bottom:10px;font-weight:700;font-size:12px;color:var(--muted);text-decoration:none}
.more::after{content:"»";font-size:15px;margin-left:2px}

/* footer */
.footer{left:0;top:805px;width:1200px;height:48px;background:var(--footer-bg);border-top:1px solid var(--footer-line);border-bottom:1px solid var(--footer-line)}
.base{left:0;top:853px;width:1200px;height:43px;background:var(--base-bg)}
.social{left:123px;top:815px;display:flex;align-items:center;font-size:12px;color:var(--ink);gap:10px;height:28px}
.social .dot{width:26px;height:26px;border-radius:50%;background:#3a86c8}
.social .sq{width:26px;height:26px;background:#e8671c;border-radius:3px;margin-left:14px}
.social b{font-weight:700}
.foot-nav{right:128px;top:822px;font-size:12px;letter-spacing:1px;word-spacing:2px;color:var(--ink)}
.foot-nav a{color:var(--ink);text-decoration:none}
.foot-nav span{margin:0 11px}
.copy{left:124px;top:862px;font-size:12px;letter-spacing:1px;color:var(--ink)}
</style>
</head>
<body>
<header>
  <div class="abs brand"><span class="brand-mark"></span><span class="brand-name">VAULTRIX</span></div>
  <nav class="abs utility"><a href="#"><i></i>Sign up</a><a href="#"><i></i>Member login</a><a href="#"><i></i>Contact us</a></nav>
  <nav class="abs nav"><a href="#">Home</a><a href="#">Remote Backup</a><a href="#">Emergency Disk</a><a href="#">Recovery</a><a href="#">Testimonials</a><a href="#">About us</a></nav>
</header>

<section>
  <div class="abs hero"></div>
  <div class="abs hero-base"></div>
  <h1 class="abs hero-title">VAULTRIX COMPUTER<br>SERVICES</h1>
  <p class="abs hero-text">It is a long established fact that a reader will be distracted by the readable content of a page when looking at its layout. The point of using Lorem Ipsum is that it has a more-or-less normal distribution</p>
  <svg class="abs cta" viewBox="0 0 276 50" aria-hidden="true">
    <path d="M4 14 H38 V4 L62 24 L38 44 V34 H4 Z" fill="#2a9be0" stroke="#1a78b8" stroke-width="1"/>
  </svg>
  <a class="abs cta-label" href="#">Backup &amp; Restore</a>
  <div class="abs product" role="img" aria-label="Backup software window with boxed product package"></div>
</section>

<main>
  <div class="abs content"></div>
  <article class="abs card services">
    <h2>Our Services</h2>
    <ul>
      <li>Reliable backup is a vital part of risk management</li>
      <li>We keep your business records safe, always</li>
      <li>Database? Customer List? Financials? Contracts?</li>
      <li>Every hard disk fails one day</li>
      <li>We backup these valuable assets</li>
      <li>Critical data backup off-site, every night</li>
      <li>Located in Perth, Western Australia- the safest<br>place on Earth</li>
    </ul>
    <a class="more" href="#">read more</a>
  </article>
  <article class="abs card about">
    <h2>About Us</h2>
    <p>It is a long established fact that a reader will be distracted by the readable content of a page when looking at its layout. The point of using Lorem Ipsum is that it has a more-or-less normal distribution of letters, as opposed to using 'Content here, content here', making it look like readable English.It is a long established fact that a reader will be distracted by the readable content of a page when looking at its layout. The point of using Lorem Ipsum is that it has a more-or-less normal distribution of letters, as opposed to using 'Content here, content here', making it look like readable English.</p>
    <a class="more" href="#">read more</a>
  </article>
  <article class="abs card testimonial">
    <h2>Testimonial</h2>
    <span class="quote open">“</span>
    <p>It is a long established fact that a reader will be distracted by the readable content of a page when looking at its layout. The point of using Lorem Ipsum is that it has a more-or-less normal distribution of letters, as opposed to using 'Content here, content here', making it look like readable English.It is a long established fact that a reader will be distracted by the readable content of a page when looking at its layout.</p>
    <span class="client">ABC Company</span>
    <span class="quote close">”</span>
    <a class="more" href="#">read more</a>
  </article>
</main>

<footer>
  <div class="abs footer"></div>
  <div class="abs base"></div>
  <div class="abs social"><span class="dot"></span><span><b>Follow Us</b> on Chirper</span><span class="sq"></span><span>or <b>RSS</b></span></div>
  <nav class="abs foot-nav"><a href="#">Home</a><span>|</span><a href="#">Remote Backup</a><span>|</span><a href="#">Emergency Disk</a><span>|</span><a href="#">Recovery</a><span>|</span><a href="#">Testimonials</a><span>|</span><a href="#">About us</a></nav>
  <p class="abs copy">©2011 - Vaultrix Computer Services</p>
</footer>
</body>
</html>
```